Natural cosmetics company is looking for a designer to produce the labels of the products and

Hello, Nus need a label and logo design for our brand RW ORGANIC. It is a brand specializing in the sale of 100% Natural cosmetic products on the internet. The first range is based on snail slime. I am looking for a clean design in green tones. The final design must be forwarded to the supplier for printing and shipping of the products. I realized a first idea for a logo, but I am interested in other ideas / suggestions. You have carte blanche :)
Here are the rules to follow for sending labels to the supplier:
• Sizes:
- Airless bottle: 10.3 x 5.5 cm
- Jar: 20x2.5cm
• Files must be in Corel Draw (. cdr) and / or vector PDF format
You must attach the file of the fonts used for the text in the label - We need this file as many fonts are difficult to find and we might need to move some text around for printing purposes
• The logo of your brand must be in a vector format along with all other components.
• Please do not add any borders or any cut marks to the design. We will do it on our end as we need to follow specific indications with our printing suppliers.
• All text and graphics must be at least 6mm from the edge
• The dimensions indicated by us must be respected in the overall size of the label
• The resolution to be used should be 300 cpi and in CMYK
• The text size should be readable and at least 4.5 points.

```html
<!DOCTYPE html>
<html lang="en">
<head>
<meta charset="utf-8">
<title>RW Organic Snail Slime Labels</title>
<link href="https://fonts.googleapis.com/css2?family=Didact+Gothic&display=swap" rel="stylesheet">
<style>
  :root {
    --paper: #ffffff;
    --backdrop: #f4f4f4;
    --ink: #1f1f1f;
    --edge: #d9d9d9;
    --leaf: #4f8a6b;
    --sketch-light: #efefef;
    --sketch-dark: #c6c6c6;
  }
  html, body {
    margin: 0;
    padding: 0;
    width: 1200px;
    height: 923px;
    overflow: hidden;
    background: var(--backdrop);
    font-family: "Didact Gothic", "Century Gothic", sans-serif;
    color: var(--ink);
  }
  .board { position: relative; width: 1200px; height: 923px; }
  .label {
    position: absolute;
    background: var(--paper);
    border: 1px solid var(--edge);
    box-sizing: border-box;
  }
  .jar-label { left: 54px; top: 54px; width: 1087px; height: 134px; }
  .bottle-label { left: 152px; top: 386px; width: 895px; height: 479px; }

  .block {
    position: absolute;
    margin: 0;
    text-align: center;
    white-space: nowrap;
    transform: translateX(-50%);
  }
  .block h3 { margin: 0; font-weight: 400; font-size: inherit; }

  .mark {
    position: absolute;
    box-sizing: border-box;
    border: 1.5px solid var(--ink);
    border-radius: 50%;
    text-align: center;
    white-space: nowrap;
    color: var(--leaf);
  }
  .sketch {
    position: absolute;
    background: radial-gradient(circle at 62% 42%, var(--sketch-dark), var(--sketch-light) 70%);
  }
  .product, .volume {
    position: absolute;
    margin: 0;
    white-space: nowrap;
    transform: translateX(-50%);
  }
  .icon {
    position: absolute;
    box-sizing: border-box;
    border-radius: 50%;
    background: var(--ink);
  }
  .icon.outline { background: none; border: 2px solid var(--ink); }
  .icon.square { border-radius: 2px; background: none; border: 1.5px solid var(--ink); }
  .address {
    position: absolute;
    margin: 0;
    writing-mode: vertical-rl;
    transform: rotate(180deg);
    white-space: nowrap;
    text-align: left;
  }

  /* jar label */
  .jar-label .block { top: 20px; font-size: 12.4px; line-height: 14.5px; }
  .jar-intro { left: 155px; }
  .jar-directions { left: 723px; }
  .jar-ingredients { left: 919px; }
  .jar-snail { left: 345px; top: 34px; width: 132px; height: 67px; border-radius: 66px 66px 14px 14px; }
  .jar-mark { left: 489px; top: 28px; width: 55px; height: 55px; font-size: 9px; line-height: 52px; }
  .jar-label .product { left: 516px; top: 89px; font-size: 10.5px; letter-spacing: 3px; }
  .jar-label .volume { left: 516px; top: 103px; font-size: 9px; }
  .jar-label .icon { left: 1016px; width: 14px; height: 14px; }
  .jar-address { left: 1044px; top: 34px; height: 84px; font-size: 8.3px; line-height: 9.5px; }

  /* bottle label */
  .bottle-intro { left: 97px; top: 34px; font-size: 16.6px; line-height: 19.7px; }
  .bottle-mark { left: 404px; top: 31px; width: 88px; height: 88px; font-size: 15px; line-height: 84px; border-width: 2px; }
  .bottle-snail { left: 356px; top: 306px; width: 184px; height: 83px; border-radius: 92px 92px 16px 16px; }
  .bottle-label .product { left: 448px; top: 415px; font-size: 15px; letter-spacing: 7px; }
  .bottle-label .volume { left: 448px; top: 436px; font-size: 14.5px; }
  .bottle-ingredients { left: 745px; top: 34px; font-size: 14.8px; line-height: 17.7px; }
  .bottle-directions { left: 745px; top: 266px; font-size: 14.8px; line-height: 17.7px; }
  .bottle-label .icon { left: 831px; width: 30px; height: 30px; }
  .bottle-address { left: 822px; top: 310px; height: 140px; font-size: 13px; line-height: 15.5px; }
</style>
</head>
<body>
<main class="board">

  <section class="label jar-label" aria-label="Jar label">
    <p class="block jar-intro">RW ORGANIC Eye Effect Day Cream<br>Lorem ipsum dolor sit amet. Dolor dolores<br>kasd sed ipsum elitr amet ut. Et eirmod at stet.<br>Ipsum est gubergren. Quis dolor amet qui<br>sadipscing suscipit dolor. Aliquip wisi vel<br>invidunt accusam augue. Nihil elitr autem.<br>Consectetuer vero elitr. Praesent vero delenit</p>
    <div class="sketch jar-snail" role="img" aria-label="Pencil sketch of a snail"></div>
    <span class="mark jar-mark">RW Organic</span>
    <p class="product">SNAIL SLIME</p>
    <p class="volume">℮ 30ml/1.01 fl.oz.</p>
    <div class="block jar-directions"><h3>DIRECTIONS:</h3>Quis dolor amet qui sadipscing<br>suscipit dolor. Aliquip wisi vel<br>invidunt accusam augue. Nihil elitr<br>autem. Consectetuer vero elitr.<br>Praesent vero delenit sed ex</div>
    <div class="block jar-ingredients"><h3>INGREDIENTS:</h3>Water,Butylene Glycol,<br>Tetrapeptide,Palmitoyl<br>Tripeptide,Collagen Amino<br>Acids,Dexpanthenol,Sodium<br>Hyaluronate,Phenoxyethanol</div>
    <span class="icon outline" style="top:22px"></span>
    <span class="icon" style="top:49px"></span>
    <span class="icon" style="top:80px"></span>
    <span class="icon square" style="top:109px"></span>
    <p class="address jar-address">RW Organic<br>Adress,adress,adress<br>MADE IN CHINA</p>
  </section>

  <section class="label bottle-label" aria-label="Airless bottle label">
    <p class="block bottle-intro">RW Organic Snail<br>Slime Lorem<br>ipsum dolor sit<br>amet. Dolor<br>dolores kasd<br>sed ipsum elitr<br>amet ut. Et<br>eirmod at stet.<br>Ipsum est<br>gubergren. Quis<br>dolor amet qui<br>sadipscing<br>suscipit dolor.<br>Aliquip wisi vel<br>invidunt accusam<br>augue. Nihil elitr<br>autem.<br>Consectetuer<br>vero elitr.<br>Praesent vero<br>delenit sed ex</p>
    <span class="mark bottle-mark">RW Organic</span>
    <div class="sketch bottle-snail" role="img" aria-label="Pencil sketch of a snail"></div>
    <p class="product">SNAIL SLIME</p>
    <p class="volume">℮ 30ml/1.01 fl.oz.</p>
    <div class="block bottle-ingredients"><h3>INGREDIENTS:</h3>Water,<br>Butylene Glycol,<br>Tetrapeptide,<br>Palmitoyl<br>Tripeptide,<br>Collagen Amino<br>Acids,Dexpanthenol,<br>Sodium<br>Hyaluronate,<br>Phenoxyethanol,<br>Ethylhexylglycerin</div>
    <div class="block bottle-directions"><h3>DIRECTIONS:</h3>Quis dolor amet<br>qui sadipscing<br>suscipit dolor.<br>Aliquip wisi vel<br>invidunt accusam<br>augue. Nihil elitr<br>autem.<br>Consectetuer vero<br>elitr. Praesent vero<br>delenit sed ex</div>
    <span class="icon outline" style="top:43px"></span>
    <span class="icon" style="top:94px"></span>
    <span class="icon" style="top:145px"></span>
    <span class="icon square" style="top:197px"></span>
    <p class="address bottle-address">RW Organic,<br>Adress,adress,adress<br>MADE IN FRANCE</p>
  </section>

</main>
</body>
</html>
```